Design a character / mascot like the Cloudmeadow Characters

Quorvo is a cloudmeadow Powered SaaS for the hospitality industry.
We would like to design a mascot for learn.quorvo.example, Quorvo online education.

https://www.cloudmeadow.example/blog/meet-pathfinder-characters-blog/

Target Market(s)

Hospitality Enterprise SaaS

Industry/Entity Type

Industry

Requirements
Must have
• Cloudmeadow characters mindset

```html
<!DOCTYPE html>
<html lang="en">
<head>
<meta charset="utf-8">
<title>Quorvo Learning – Courses</title>
<link href="https://fonts.googleapis.com/css2?family=Lato:wght@400;700&family=Poppins:wght@500;600;700&family=Merriweather:wght@300&display=swap" rel="stylesheet">
<style>
  :root {
    --lavender: #c5cbfa;
    --white: #ffffff;
    --plum: #45334f;
    --plum-dim: #3a2b42;
    --ink: #2f2233;
    --pink: #ec5a7c;
    --text: #3c3c3c;
    --muted: #6f6f6f;
    --hover-grey: #a3a3a3;
    --giraffe-orange: #f6a93b;
    --star: #f4b63e;
  }
  * { box-sizing: border-box; margin: 0; padding: 0; }
  html, body { width: 1200px; height: 1200px; overflow: hidden; background: var(--white); }
  .canvas { position: relative; width: 1200px; height: 1200px; overflow: hidden; }
  .backdrop { position: absolute; inset: 0; }

  .site-panel {
    position: absolute; left: 28px; top: 308px; width: 1144px; height: 584px;
    background: var(--white); overflow: hidden; font-family: "Lato", sans-serif;
  }
  .brand {
    position: absolute; left: 222px; top: 14px;
    display: flex; align-items: center; gap: 8px;
    font-family: "Poppins", sans-serif; font-weight: 600; font-size: 38px; color: var(--ink);
    letter-spacing: -0.5px;
  }
  .brand-dot { width: 10px; height: 10px; background: var(--pink); }
  .nav { position: absolute; right: 226px; top: 26px; display: flex; gap: 17px; font-size: 12px; color: var(--pink); }
  .page-title {
    position: absolute; left: 0; right: 0; top: 112px; text-align: center;
    font-size: 22px; color: var(--ink); font-weight: 400;
  }
  .mascot-slot {
    position: absolute; left: 58px; top: 230px; width: 150px; height: 336px;
    border-radius: 70px 70px 20px 20px;
    background: linear-gradient(180deg, var(--giraffe-orange) 0%, #f2b24a 45%, #ecebf3 62%, #d9d9e4 100%);
  }
  .status-url {
    position: absolute; left: 0; bottom: 0; width: 194px; height: 7px;
    background: #eeeeee; font-size: 5px; line-height: 7px; color: var(--muted); padding-left: 2px; white-space: nowrap; overflow: hidden;
  }

  .course-grid {
    position: absolute; left: 221px; top: 160px;
    display: grid; grid-template-columns: repeat(3, 220px); column-gap: 21px; row-gap: 15px;
  }
  .course-card { background: var(--white); box-shadow: 0 1px 3px rgba(0,0,0,0.12); height: 242px; overflow: hidden; }
  .course-banner {
    height: 124px; background: var(--plum); color: var(--white); text-align: center;
    display: flex; flex-direction: column; align-items: center; padding-top: 11px;
  }
  .banner-brand { font-family: "Poppins", sans-serif; font-weight: 500; font-size: 19px; line-height: 24px; }
  .banner-role {
    flex: 1; display: flex; align-items: center; justify-content: center;
    font-family: "Poppins", sans-serif; font-weight: 700; font-size: 22px; line-height: 29px; padding: 0 10px 8px;
  }
  .course-body { padding: 9px 10px; }
  .course-name { font-family: "Merriweather", serif; font-weight: 300; font-size: 13px; line-height: 15px; color: var(--text); }
  .course-kind { display: flex; align-items: center; gap: 5px; font-size: 8px; color: var(--muted); margin-top: 2px; }
  .course-kind svg { width: 8px; height: 8px; }
  .rating { display: flex; align-items: center; gap: 4px; font-size: 8px; color: var(--text); margin-top: 9px; }
  .rating svg { width: 8px; height: 8px; }
  .course-summary { font-size: 10.5px; line-height: 16.5px; color: var(--text); margin-top: 10px; }

  .course-card.is-hovered .course-banner { background: var(--plum-dim); }
  .course-card.is-hovered .course-body { background: var(--hover-grey); height: 118px; }
  .course-card.is-hovered .course-name,
  .course-card.is-hovered .course-summary { color: #3b3b3b; }
  .course-card.is-hovered .course-kind { color: #4a4a4a; }
</style>
</head>
<body>
<div class="canvas">
  <svg class="backdrop" width="1200" height="1200" viewBox="0 0 1200 1200" aria-hidden="true">
    <rect x="0" y="0" width="1200" height="310" fill="var(--lavender)"/>
    <path d="M1160 300 L1200 300 L1200 462 Q1185 456 1165 458 Z" fill="var(--lavender)"/>
    <path d="M0 888 L278 888 Q215 1010 203 1200 L0 1200 Z" fill="var(--lavender)"/>
  </svg>

  <div class="site-panel">
    <div class="brand">Quorvo<span class="brand-dot"></span></div>
    <nav class="nav"><span>All Courses</span><span>Sign In</span></nav>
    <h1 class="page-title">Courses</h1>

    <div class="mascot-slot" role="img" aria-label="Mascot illustration: a cartoon giraffe in a white lab coat holding a pointer stick"></div>

    <div class="course-grid">
      <article class="course-card">
        <div class="course-banner"><div class="banner-brand">Quorvo</div><div class="banner-role">Sales<br>Managers</div></div>
        <div class="course-body">
          <h2 class="course-name">Quorvo for Sales Managers</h2>
          <div class="course-kind"><svg viewBox="0 0 8 8"><rect x="0.5" y="0.5" width="7" height="5.5" fill="none" stroke="#888" stroke-width="0.8"/><path d="M2 6 L2 7.5 L3.5 6" fill="none" stroke="#888" stroke-width="0.8"/></svg>Course</div>
          <div class="rating"><svg viewBox="0 0 10 10"><path d="M5 0.5 L6.3 3.6 L9.6 3.8 L7 6 L7.9 9.3 L5 7.5 L2.1 9.3 L3 6 L0.4 3.8 L3.7 3.6 Z" fill="var(--star)"/></svg>5.0 (2 reviews)</div>
          <p class="course-summary">This course is designed for Sales Managers. It will help you understand how you can use Quorvo to run your day to day…</p>
        </div>
      </article>

      <article class="course-card">
        <div class="course-banner"><div class="banner-brand">Quorvo</div><div class="banner-role">Catering<br>Managers</div></div>
        <div class="course-body">
          <h2 class="course-name">Quorvo for Catering Managers</h2>
          <div class="course-kind"><svg viewBox="0 0 8 8"><rect x="0.5" y="0.5" width="7" height="5.5" fill="none" stroke="#888" stroke-width="0.8"/><path d="M2 6 L2 7.5 L3.5 6" fill="none" stroke="#888" stroke-width="0.8"/></svg>Course</div>
          <p class="course-summary">This course is designed for Catering Managers. It will help you understand how to manage everything to do with…</p>
        </div>
      </article>

      <article class="course-card is-hovered">
        <div class="course-banner"><div class="banner-brand">Quorvo</div><div class="banner-role">Assistants &amp;<br>Coordinators</div></div>
        <div class="course-body">
          <h2 class="course-name">Quorvo for Sales Assistants &amp; Coordinators</h2>
          <div class="course-kind"><svg viewBox="0 0 8 8"><rect x="0.5" y="0.5" width="7" height="5.5" fill="none" stroke="#555" stroke-width="0.8"/><path d="M2 6 L2 7.5 L3.5 6" fill="none" stroke="#555" stroke-width="0.8"/></svg>Course</div>
          <p class="course-summary">This course is designed for Sales Assistants and Coordinators. It will help you understand how to use Quorvo to run…</p>
        </div>
      </article>

      <article class="course-card">
        <div class="course-banner"><div class="banner-brand">Quorvo</div><div class="banner-role">Directors of Sales</div></div>
        <div class="course-body">
          <h2 class="course-name">Quorvo for Directors of Sales</h2>
          <div class="course-kind"><svg viewBox="0 0 8 8"><rect x="0.5" y="0.5" width="7" height="5.5" fill="none" stroke="#888" stroke-width="0.8"/><path d="M2 6 L2 7.5 L3.5 6" fill="none" stroke="#888" stroke-width="0.8"/></svg>Course</div>
        </div>
      </article>

      <article class="course-card">
        <div class="course-banner"><div class="banner-brand">Quorvo</div><div class="banner-role">Directors of<br>Catering</div></div>
        <div class="course-body">
          <h2 class="course-name">Quorvo for Directors of Catering</h2>
          <div class="course-kind"><svg viewBox="0 0 8 8"><rect x="0.5" y="0.5" width="7" height="5.5" fill="none" stroke="#888" stroke-width="0.8"/><path d="M2 6 L2 7.5 L3.5 6" fill="none" stroke="#888" stroke-width="0.8"/></svg>Course</div>
        </div>
      </article>

      <article class="course-card">
        <div class="course-banner"><div class="banner-brand">Quorvo</div><div class="banner-role">Property<br>Admins</div></div>
        <div class="course-body">
          <h2 class="course-name">Quorvo for Property Admins</h2>
          <div class="course-kind"><svg viewBox="0 0 8 8"><rect x="0.5" y="0.5" width="7" height="5.5" fill="none" stroke="#888" stroke-width="0.8"/><path d="M2 6 L2 7.5 L3.5 6" fill="none" stroke="#888" stroke-width="0.8"/></svg>Course</div>
        </div>
      </article>
    </div>

    <div class="status-url">https://learn.quorvo.example/courses/quorvo-for-sales-assistants</div>
  </div>
</div>
</body>
</html>
```